Health and Wellness company needs flyer to promote free seminar

Stride reform studio is a health and wellness company that offers an exercise program designed by physical therapists to help relieve pain and improve mobility. Our business is a new concept that is not well understood by the public. In order to promote our business we offer a free seminar where we present information regarding the underlying cause of pain and tightness. During the seminar we also perform a posture screen and movement testing for all participants.

Target Market(s)

Mostly healthy and active women ages 25-65

Industry/Entity Type

Health And Wellness

Font styles to use
Sans Serif

Colors

Designer to choose colors to be used in the design.

Requirements
Must have
• Title: Eliminate Pain and Tightness For Good
• Paragraph: Stride Reform Studio offers a free 60 minute seminar: "The Busy Walker's Handbook to Bending and Standing Taller."
• What to Expect:
• • Identify the underlying cause of your pain and mobility issues
• • Expose what gets in the way of you moving and feeling better
• • Learn why traditional exercises don’t help and can actually make the problem worse
• • Reveal what your posture is saying and how that impacts you
• • Experience your muscle imbalances through movement tests
• • Discover the training method that realigns your posture, increases your mobility and reduces your pain
• Call to action: RSVP online at stridereformstudio.com
Nice to have
• Use a relevant image showing a female dealing with tightness in the low back, legs, etc.
• Emphasize that the seminar is FREE.
• Make the call to action prominent.

```html
<!DOCTYPE html>
<html lang="en">
<head>
<meta charset="utf-8">
<title>Stride Reform Studio – Free Seminar Flyer</title>
<link href="https://fonts.googleapis.com/css2?family=Lato:wght@400;700;900&display=swap" rel="stylesheet">
<style>
  :root{
    --orange:#f7931e;
    --orange-deep:#ef7f12;
    --purple:#5b5bb5;
    --ink:#333333;
    --footer:#4b4b4b;
    --paper:#ffffff;
    --backdrop:#c9c9c9;
  }
  *{margin:0;padding:0;box-sizing:border-box}
  html,body{width:1200px;height:1200px;overflow:hidden;background:var(--backdrop);font-family:"Lato",sans-serif}
  .flyer{position:absolute;left:200px;top:41px;width:463px;height:647px;background:var(--paper);
    transform:scale(1.728);transform-origin:0 0;box-shadow:0 1px 3px rgba(0,0,0,.3);overflow:hidden}
  .shapes{position:absolute;inset:0}
  .abs{position:absolute}
  .brand{left:230px;top:236px;display:flex;align-items:center;gap:7px}
  .brand-mark{width:26px;height:26px;border:3px solid var(--purple)}
  .brand-name{font-weight:700;font-size:17px;color:var(--purple)}
  .headline{left:226px;width:214px;top:286px;text-align:center;color:var(--ink)}
  .headline .line1{font-weight:900;font-size:24px;line-height:1.1}
  .headline .line2{font-weight:400;font-size:20px;color:var(--purple);line-height:1.05}
  .headline .line3{font-weight:900;font-size:34px;line-height:1.05}
  .expect-title{left:226px;width:214px;top:384px;text-align:center;font-size:28px;color:var(--orange);font-weight:400}
  .expect-list{left:236px;top:423px;width:204px;list-style:none;font-size:7.1px;line-height:1.25;color:var(--ink)}
  .expect-list li{position:relative;padding-left:8px;margin-bottom:1.6px}
  .expect-list li::before{content:"";position:absolute;left:0;top:1.8px;width:4px;height:4px;background:var(--orange)}
  .phones{left:243px;top:545px;width:193px;height:20px;border:1.3px solid var(--purple);border-radius:10px;
    display:flex;align-items:center;justify-content:center;gap:6px;font-size:10px;color:var(--ink);
    box-shadow:0 3px 3px -2px rgba(0,0,0,.25)}
  .phones .sep{width:1px;height:11px;background:var(--purple)}
  .phones svg{width:8px;height:8px;vertical-align:-1px;margin-right:2px}
  .badge-text{left:54px;top:350px;width:116px;text-align:center;color:#fff}
  .badge-text .free{font-weight:900;font-size:32px;line-height:1}
  .badge-text .sub{font-weight:700;font-size:13px;line-height:1.15;color:var(--ink)}
  .guide{left:10px;width:196px;top:450px;text-align:center;color:var(--ink)}
  .guide .intro{font-size:15.5px;font-weight:400}
  .guide .boxed{display:block;background:var(--purple);color:#fff;font-weight:900;margin:2px auto 0;width:187px}
  .guide .big{font-size:30px;line-height:40px}
  .guide .and{font-size:16px;line-height:20px}
  .guide .mid{font-size:23px;line-height:30px}
  .cta{left:0;top:582px;width:463px;height:28px;background:var(--orange);color:#fff;text-align:center;
    font-size:15px;font-weight:700;line-height:28px}
  .cta strong{font-weight:900}
  .footer{left:0;top:610px;width:463px;height:37px;background:var(--footer);color:#fff;font-size:6.4px;line-height:1.35}
  .footer .item{position:absolute;top:10px}
  .footer svg{width:6px;height:6px;vertical-align:-1px}
</style>
</head>
<body>
<main class="flyer">
  <svg class="shapes" viewBox="0 0 463 647" width="463" height="647" aria-hidden="false">
    <defs>
      <linearGradient id="posture-photo" x1="0" y1="0" x2="1" y2="1">
        <stop offset="0" stop-color="#e6e3df"/><stop offset=".45" stop-color="#c9b79f"/>
        <stop offset=".6" stop-color="#3f5a8f"/><stop offset="1" stop-color="#2c4070"/>
      </linearGradient>
      <linearGradient id="runner-photo" x1="0" y1="0" x2="1" y2="1">
        <stop offset="0" stop-color="#b0824e"/><stop offset=".5" stop-color="#3a3434"/><stop offset="1" stop-color="#b38a5c"/>
      </linearGradient>
      <linearGradient id="orange-tint" x1="0" y1="0" x2="1" y2="1">
        <stop offset="0" stop-color="#f7931e"/><stop offset="1" stop-color="#ee7a10"/>
      </linearGradient>
    </defs>
    <polygon class="accent-block" points="0,0 138,0 138,85 0,165" fill="url(#orange-tint)"/>
    <polygon class="accent-strip" points="430,0 463,0 463,135 430,155" fill="var(--orange)"/>
    <polygon role="img" aria-label="Photo of a woman at a desk holding her lower back" points="155,0 420,0 420,150 290,225 155,150" fill="url(#posture-photo)"/>
    <polygon role="img" aria-label="Photo of a runner crouching on sand holding her knee" points="0,170 104,137 206,196 206,330 104,392 0,332" fill="url(#runner-photo)"/>
    <polygon class="free-badge" points="112,319 168,351 168,414 112,446 56,414 56,351" fill="var(--orange)" stroke="var(--purple)" stroke-width="4"/>
  </svg>

  <div class="abs badge-text">
    <div class="free">FREE</div>
    <div class="sub">60 MINUTE<br>SEMINAR</div>
  </div>

  <div class="abs brand">
    <span class="brand-mark"></span>
    <span class="brand-name">Stride Reform Studio</span>
  </div>

  <h1 class="abs headline">
    <div class="line1">ELIMINATE PAIN</div>
    <div class="line2">And Tightness</div>
    <div class="line3">FOR GOOD</div>
  </h1>

  <h2 class="abs expect-title">What to Expect</h2>
  <ul class="abs expect-list">
    <li>Identify the underlying cause of your pain and mobility issues</li>
    <li>Expose what gets in the way of you moving and feeling better</li>
    <li>Learn why traditional exercises don't help and can actually make the problem worse</li>
    <li>Reveal what your posture is saying and how that impacts you</li>
    <li>Experience your muscle imbalances through movement tests</li>
    <li>Discover the training method that realigns your posture, increases your mobility and reduces your pain</li>
  </ul>

  <div class="abs phones">
    <span><svg viewBox="0 0 10 10"><path d="M2 1l2 2-1 1.2c.6 1.2 1.6 2.2 2.8 2.8L7 6l2 2-1.2 1.2C4.5 9 1 5.5.8 2.2z" fill="var(--purple)"/></svg>(281) 555-0142</span>
    <span class="sep"></span>
    <span><svg viewBox="0 0 10 10"><path d="M2 1l2 2-1 1.2c.6 1.2 1.6 2.2 2.8 2.8L7 6l2 2-1.2 1.2C4.5 9 1 5.5.8 2.2z" fill="var(--purple)"/></svg>(503) 555-0187</span>
  </div>

  <div class="abs guide">
    <div class="intro">The Busy Walker's Handbook</div>
    <span class="boxed big">to Bending</span>
    <div class="and">and</div>
    <span class="boxed mid">Standing Taller</span>
  </div>

  <div class="abs cta">Sign up online at <strong>stridereformstudio.com/free-seminar</strong></div>

  <footer class="abs footer">
    <div class="item" style="left:27px"><svg viewBox="0 0 10 10"><path d="M5 0a3.5 3.5 0 0 1 3.5 3.5C8.5 6 5 10 5 10S1.5 6 1.5 3.5A3.5 3.5 0 0 1 5 0z" fill="#fff"/></svg>1480 Larkfield Avenue<br>&nbsp;&nbsp;Houston, TX 77000</div>
    <div class="item" style="left:134px"><svg viewBox="0 0 10 10"><path d="M5 0a3.5 3.5 0 0 1 3.5 3.5C8.5 6 5 10 5 10S1.5 6 1.5 3.5A3.5 3.5 0 0 1 5 0z" fill="#fff"/></svg>2205 SE Alder Lane #12<br>&nbsp;&nbsp;Milwaukie, OR 97000</div>
    <div class="item" style="left:245px"><svg viewBox="0 0 10 10"><circle cx="5" cy="5" r="4" fill="none" stroke="#fff" stroke-width="1.4"/></svg> http://www.stridereformstudio.com/contact-us.html</div>
  </footer>
</main>
</body>
</html>
```